Website design to promote trampoline business

We require a website design for our business. The business is primarily provising access for people between 5YO and 40YO to jump on trampolines for fun and fitness.

We have a logo and color schemes already and the website should incorporate these colors and designs.

We would like to incorporate the following pages:-

Book Now!
Home
About Us
Locations & Hours
Jumping
Groups & Events
Gallery
Safety
Latest News
Careers

Industry/Entity Type

Business

Requirements
Must have
• Incorporate our logo and colors (files attached).

```html
<!DOCTYPE html>
<html lang="en">
<head>
<meta charset="utf-8">
<title>Bounce Hub Trampolines</title>
<link href="https://fonts.googleapis.com/css2?family=Open+Sans:ital,wght@0,400;0,600;0,700;0,800;1,600&display=swap" rel="stylesheet">
<style>
:root{
  --canvas:#e9eaec;
  --page:#ffffff;
  --blue:#2b8fd8;
  --blue-dark:#1c74b8;
  --blue-soft:#e7f2fb;
  --orange:#f39a1e;
  --ink:#444a50;
  --muted:#8a9096;
  --dark:#2f3336;
  --line:#dde2e6;
}
*{box-sizing:border-box;margin:0;padding:0}
html,body{width:889px;height:1200px;overflow:hidden;background:var(--canvas);font-family:"Open Sans",Arial,sans-serif;color:var(--ink)}
.page{position:absolute;left:140px;top:8px;width:610px;height:1180px;background:var(--page);box-shadow:0 0 6px rgba(0,0,0,.12)}
.abs{position:absolute}
/* header */
.brand{left:14px;top:16px;display:flex;align-items:center;gap:7px;font-weight:800;font-size:25px;color:var(--blue);letter-spacing:.5px}
.brand .mark{width:18px;height:18px;background:var(--blue)}
.social{right:14px;top:12px;display:flex;gap:4px}
.social span{width:11px;height:11px;border-radius:50%;background:#c7ccd1}
.contact{right:14px;top:30px;width:230px;text-align:right;font-size:6.5px;line-height:10px;color:var(--muted)}
/* nav */
.nav{left:0;top:66px;width:610px;height:22px;background:var(--blue);display:flex;padding-left:14px}
.nav a{font-size:7.5px;color:#fff;text-decoration:none;padding:0 9px;line-height:22px;font-weight:600}
.nav a.active{background:var(--blue-dark)}
/* hero */
.hero{left:0;top:90px;width:610px;height:302px;background:linear-gradient(180deg,#8cc6ec 0%,#b7dcf3 45%,#d9ecf6 70%,#9fb69a 100%)}
.hero-head{right:18px;top:118px;width:250px;padding:8px 12px;background:rgba(43,143,216,.9);color:#fff;font-style:italic;font-weight:600;font-size:19px;line-height:23px}
.booking{left:0;top:232px;width:610px;height:58px;background:rgba(40,44,48,.82);padding:9px 14px;color:#fff}
.booking h2{font-size:11px;font-weight:600}
.booking p{font-size:6.5px;line-height:9px;color:#cfd4d8;width:440px;margin-top:5px}
.btn{display:inline-block;background:var(--orange);color:#fff;font-weight:700;font-size:8px;text-align:center;border-radius:2px}
.booking .btn{position:absolute;right:14px;top:16px;width:70px;height:24px;line-height:24px;font-size:9px}
.dots{left:0;top:296px;width:610px;display:flex;justify-content:center;gap:4px}
.dots span{width:5px;height:5px;border-radius:50%;background:#c5ccd2}
.dots span.on{background:var(--blue)}
/* groups */
.section-title{font-size:10px;font-weight:700;color:var(--blue)}
.groups-title{left:14px;top:404px}
.cards{left:14px;top:420px;width:582px;display:grid;grid-template-columns:repeat(4,1fr);gap:10px}
.card .photo{height:80px}
.card h3{font-size:7.5px;color:var(--blue);font-weight:700;margin-top:6px}
.card .date{font-size:6px;color:var(--muted);margin-top:2px}
.card p{font-size:6px;line-height:8.5px;margin-top:3px}
/* testimonials */
.testimonials{left:14px;top:582px;width:582px;height:66px;border:1px solid var(--line);border-left:3px solid var(--blue);background:#f7f9fb;padding:9px 12px}
.testimonials h2{font-size:9px;color:var(--blue);font-weight:700}
.testimonials p{font-size:6.5px;line-height:9px;width:400px;margin-top:4px;color:var(--muted)}
.testimonials .btn{position:absolute;right:12px;top:20px;width:108px;height:24px;line-height:24px;background:var(--blue)}
/* about column */
.about-photo{left:14px;top:664px;width:188px;height:170px;background:linear-gradient(160deg,#9fcde9,#cbe3c3 60%,#8fb77c)}
.about{left:14px;top:834px;width:188px;height:226px;background:var(--blue);color:#fff;padding:14px 12px}
.about h2{font-size:10px;font-weight:700}
.about p{font-size:6.5px;line-height:9.5px;margin-top:8px;color:#e3f0fa}
.about .btn{margin-top:12px;width:58px;height:18px;line-height:18px}
/* feature columns */
.feature{top:662px;width:186px}
.feature h2{font-size:10px;font-weight:600;color:var(--blue);text-align:center}
.feature .photo{height:150px;margin-top:8px}
.feature p{font-size:6.5px;line-height:9px;margin-top:7px}
.feature .btn{margin-top:9px;width:52px;height:16px;line-height:16px;background:#e4e8eb;color:var(--ink);font-weight:600;font-size:7px}
/* locations */
.locations{left:212px;top:960px;width:384px;height:100px;background:var(--blue-soft);display:flex}
.map{width:96px;height:100px;background:linear-gradient(135deg,#dfe6d5,#cfdcc6 50%,#c2d6e6)}
.loc-info{padding:22px 12px;flex:1}
.loc-info h2{font-size:10px;color:var(--blue);font-weight:600}
.loc-info p{font-size:6.5px;line-height:10px;margin-top:4px;display:flex;align-items:center;gap:4px}
.hours{width:110px;background:var(--blue);color:#fff;padding:18px 12px;font-size:7px;line-height:11px}
.hours b{font-size:8px}
/* footer */
.footer{left:0;top:1092px;width:610px;height:88px;background:var(--dark);padding:16px 14px}
.footer-brand{font-weight:800;font-size:15px;color:#7c8389;display:flex;align-items:center;gap:6px}
.footer-brand .mark{width:12px;height:12px;background:#7c8389}
.footer-nav{position:absolute;left:150px;top:20px;display:flex}
.footer-nav a{font-size:6.5px;color:#b9bfc4;text-decoration:none;padding:0 7px;border-left:1px solid #555b60}
.footer-nav a:first-child{border-left:0;padding-left:0}
.copy{position:absolute;left:150px;top:38px;font-size:6px;color:#8b9196}
</style>
</head>
<body>
<div class="page">
  <header>
    <div class="abs brand"><span class="mark"></span>BOUNCE HUB</div>
    <div class="abs social"><span></span><span></span><span></span><span></span></div>
    <div class="abs contact">12 Spring Lane, Hopton Park, Westvale<br>(+00) 1234 5678 &nbsp; hello@bouncehubtramp.example</div>
  </header>
  <nav class="abs nav">
    <a class="active">Home</a><a>About Us</a><a>Locations &amp; Hours</a><a>Jumping</a><a>Groups &amp; Events</a><a>Gallery</a><a>Safety</a><a>Latest News</a><a>Careers</a>
  </nav>

  <section class="abs hero" role="img" aria-label="Photo of a girl jumping on an outdoor trampoline against a blue sky">
    <div class="abs hero-head">Our customers are people from 5yrs to 40yrs.</div>
    <div class="abs booking">
      <h2>Bounce Hub Trampolines Booking</h2>
      <p>Jump sessions run every day of the week. Book a time for your family, friends or team and arrive ready to bounce, play and stay fit with us all year.</p>
      <span class="btn">Book Now</span>
    </div>
  </section>
  <div class="abs dots"><span class="on"></span><span></span><span></span><span></span></div>

  <h2 class="abs section-title groups-title">Groups &amp; Events</h2>
  <div class="abs cards">
    <article class="card"><div class="photo" role="img" aria-label="Photo of kids jumping together" style="background:linear-gradient(160deg,#a8d2ee,#6e9fc7)"></div><h3>It's a long weekend fun!</h3><div class="date">12 Feb 2024</div><p>Bring the whole crew for a day of jumping, games and snacks at our park.</p></article>
    <article class="card"><div class="photo" role="img" aria-label="Photo of a family outdoors" style="background:linear-gradient(160deg,#b9dcf2,#7fa36b)"></div><h3>It's a long weekend fun!</h3><div class="date">12 Feb 2024</div><p>Bring the whole crew for a day of jumping, games and snacks at our park.</p></article>
    <article class="card"><div class="photo" role="img" aria-label="Photo of a child mid-air on a trampoline" style="background:linear-gradient(160deg,#9cc8e8,#d8e4ee)"></div><h3>It's a long weekend fun!</h3><div class="date">12 Feb 2024</div><p>Bring the whole crew for a day of jumping, games and snacks at our park.</p></article>
    <article class="card"><div class="photo" role="img" aria-label="Photo of a group of friends in a circle" style="background:linear-gradient(160deg,#8ec3e6,#c4d9a9)"></div><h3>It's a long weekend fun!</h3><div class="date">12 Feb 2024</div><p>Bring the whole crew for a day of jumping, games and snacks at our park.</p></article>
  </div>

  <section class="abs testimonials">
    <h2>Testimonials</h2>
    <p>"Our kids had the best afternoon ever. Friendly staff, safe equipment and plenty of space to play. We will be back for the next holiday for sure." — Parent</p>
    <span class="btn">Click here for more</span>
  </section>

  <div class="abs about-photo" role="img" aria-label="Photo of smiling kids outdoors"></div>
  <section class="abs about">
    <h2>About Bounce Hub Trampolines</h2>
    <p>We are a local trampoline park built for fun and fitness. Everyone from five to forty can jump, flip and play in a safe space run by trained staff. Our sessions suit families, schools, parties and anyone who wants to keep active while having a great time.</p>
    <span class="btn">Read More</span>
  </section>

  <section class="abs feature" style="left:212px">
    <h2>Careers</h2>
    <div class="photo" role="img" aria-label="Photo of a kid jumping in a yard" style="background:linear-gradient(160deg,#a4d0ee,#85ad74)"></div>
    <p>Join our friendly team and help people jump safely every day. We hire floor staff, coaches and party hosts across all our sites. Training is given on the job, shifts are flexible and every role comes with free jump time for you and your family.</p>
    <span class="btn">Read More</span>
  </section>
  <section class="abs feature" style="left:410px">
    <h2>Jumping</h2>
    <div class="photo" role="img" aria-label="Photo of a trampoline in a garden" style="background:linear-gradient(160deg,#b3d8f0,#6f9a63)"></div>
    <p>Free jump, fitness classes and toddler time. Pick a session that suits you and enjoy the bounce with friends and family. Grip socks are provided, staff watch every court and new jumpers get a short safety talk first.</p>
    <span class="btn">Read More</span>
  </section>

  <section class="abs locations">
    <div class="map" role="img" aria-label="Map showing the park location"></div>
    <div class="loc-info">
      <h2>Locations &amp; Hours</h2>
      <p><svg width="7" height="9" viewBox="0 0 7 9"><path d="M3.5 0A3.5 3.5 0 0 0 0 3.5C0 6 3.5 9 3.5 9S7 6 7 3.5A3.5 3.5 0 0 0 3.5 0z" fill="#2b8fd8"/><circle cx="3.5" cy="3.5" r="1.3" fill="#fff"/></svg>12 Spring Lane, Hopton Park, Westvale</p>
      <p><svg width="8" height="8" viewBox="0 0 8 8"><path d="M1.5 0.5l1.4 0 .6 1.8-.9.7a4.5 4.5 0 0 0 2.4 2.4l.7-.9 1.8.6v1.4c0 .5-.5 1-1 1A6.5 6.5 0 0 1 .5 1.5c0-.5.5-1 1-1z" fill="#2b8fd8"/></svg>(+00) 1234 5678</p>
    </div>
    <div class="hours"><b>Mon - Fri</b><br>10am - 8pm<br><b>Sat - Sun</b><br>9am - 9pm</div>
  </section>

  <footer class="abs footer">
    <div class="footer-brand"><span class="mark"></span>BOUNCE HUB</div>
    <nav class="footer-nav"><a>Home</a><a>About Us</a><a>Locations &amp; Hours</a><a>Jumping</a><a>Groups &amp; Events</a><a>Gallery</a><a>Safety</a><a>Latest News</a><a>Careers</a></nav>
    <div class="copy">Copyright 2024 © Bounce Hub Trampolines. All rights reserved.</div>
  </footer>
</div>
</body>
</html>
```